Therapy Dog Business need a brochure

I need a brochure designed for my Canine Assisted Therapy business in Victoria Australia. I have a logo already and info and photos to upload.
Best as white background and using the colours from the logo please
Updates

Hi Everyone,
I am sorry to have to revise the brief. I have added three new photos I was unable to add due to the size. I have had to wait for my photographer to change the size to add them today. I have been really inspired by all the work you have done so far. Thank you.
Could you please add the following on the brochure. (Under the individual dogs photo)
1. Pebble is the white dog. Please add the following under her picture. Pebble is one of the first Court Dogs in Australia. Working in Victoria, she has worked in the following Courts. The Inquest Tribunal of Norvale, The Petty Sessions Bench in Collingwood, and the Shire Tribunal in Melbourne CBD. Her ability to use her intuition for clients is inspiring. Please contact us for potential use in Courts. Pebble has worked at the Halden Constabulary College, and at KESTREL at Hal Con. She is a stunning dog!
2. Tobias is the golden dog. Tobias is Pebbles son, and had her instinct of intuition of who needs his help. Tobias has an incredible soft approach as does his mother Pebble. He is incredibly safe with young children, and yet has a playful nature for adolescents and adults alike. He is soft and caring, and like his mother will go to those who need him most. Tobias like his mother has worked at Halden Constabulary, his time at HC included the Halden Constabulary Command (HCC) Both he and his mother have very impressive CV'S!
3. Clover the black dog. Clover is my Therapy and Assistance dog "trainer" she is safe and stable with all the dogs and people I train for Therapy Dog Training and Assistance Dog Training. She has also been with me on my journey as a Counsellor and I have been able to work alongside her and Pebble for Counselling sessions.
She is soft, caring, and also intuitive. I am incredibly grateful for her help, as well as Pebble and Tobias.
ALSO I am so sorry to add this but could you also add the following: Maybe in dot point?
Court Dog Availability
Therapy Dog Visits - Lawyers - Courts - Child Protection
Police Station / Ambulance Station / Fire Station - Visits
Private Therapy Dog Sessions
website and email confirmation coming soon. Thank you

Target Market(s)

First Responders

Requirements
Must have
• All the photos provided.
Should not have
• Generic photos

```html
<!DOCTYPE html>
<html lang="en">
<head>
<meta charset="utf-8">
<title>Canine Assisted Therapy – Brochure Panel</title>
<link rel="stylesheet" href="https://fonts.googleapis.com/css2?family=Montserrat:wght@400;500;700&display=swap">
<style>
  :root {
    --page-bg: #e6e6e8;
    --card-white: #ffffff;
    --panel-cream: #f3f1ec;
    --box-white: #fbfbf9;
    --ink: #1d1d1d;
    --maroon: #3a1620;
    --rule-taupe: #9a8f87;
    --rule-light: #c9c3bd;
    --leaf-red: #a3281f;
    --photo-blue: #8fa6d8;
    --photo-brick: #a0623f;
  }
  * { box-sizing: border-box; margin: 0; padding: 0; }
  html, body { width: 1200px; height: 1000px; overflow: hidden; }
  body {
    background: var(--page-bg);
    font-family: "Montserrat", Arial, sans-serif;
    color: var(--ink);
    position: relative;
  }
  .brochure {
    position: absolute; left: 22px; top: 92px; width: 1156px; height: 816px;
    background: var(--card-white);
  }
  .brochure__panel {
    position: absolute; left: 24px; top: 24px; width: 1108px; height: 768px;
    background: var(--panel-cream);
  }
  .intro {
    position: absolute; left: 16px; top: 14px; width: 330px; height: 740px;
    background: var(--card-white);
  }
  .photo {
    position: absolute; background: var(--card-white); padding: 6px;
    box-shadow: 0 3px 8px rgba(0,0,0,.3);
  }
  .photo__fill { width: 100%; height: 100%; }
  .photo--black-dog { left: 16px; top: 108px; width: 164px; height: 126px; transform: rotate(-2deg); }
  .photo--black-dog .photo__fill { background: linear-gradient(180deg, var(--photo-brick) 0%, #5a3a2c 55%, #1a1a1a 60%, #24293a 100%); }
  .photo--white-dog { left: 138px; top: 28px; width: 172px; height: 140px; transform: rotate(2deg); }
  .photo--white-dog .photo__fill { background: linear-gradient(180deg, var(--photo-blue) 0%, #d8cdb8 45%, #efe8da 100%); }
  .leaf-mark {
    position: absolute; left: 198px; top: 168px; width: 48px; height: 48px;
    border-radius: 50%;
    background: radial-gradient(circle, var(--leaf-red) 0%, var(--leaf-red) 45%, rgba(163,40,31,0) 72%);
  }
  .intro__title {
    position: absolute; left: 32px; top: 258px; width: 290px;
    font-weight: 700; font-size: 26px; line-height: 30px; color: var(--maroon);
  }
  .intro__text {
    position: absolute; left: 32px; top: 323px; width: 300px;
    font-size: 16.5px; line-height: 28.85px; white-space: nowrap;
  }
  .benefits {
    position: absolute; left: 372px; top: 38px; width: 722px;
    border-top: 1px solid var(--rule-light);
  }
  .section-title {
    font-weight: 700; font-size: 33px; line-height: 40px; color: var(--maroon);
  }
  .benefits .section-title {
    padding: 10px 0 10px 2px;
    border-bottom: 3px solid var(--rule-taupe);
  }
  .point-list { list-style: none; }
  .point-list li { position: relative; white-space: nowrap; }
  .point-list li::before {
    content: ""; position: absolute; left: -11px; top: 11px;
    width: 4px; height: 4px; border-radius: 50%; background: var(--maroon);
  }
  .point-list strong { font-weight: 700; color: var(--maroon); }
  .benefits .point-list { margin: 10px 0 0 14px; font-size: 16.4px; line-height: 24px; }
  .benefits .point-list li + li { margin-top: 9px; }
  .why {
    position: absolute; left: 378px; top: 454px; width: 712px; height: 298px;
    background: var(--box-white); border: 1px solid var(--rule-light);
    padding: 12px 0 0 20px;
  }
  .why .point-list { margin: 8px 0 0 12px; font-size: 16.4px; line-height: 24px; }
  .why .point-list li + li { margin-top: 13px; }
</style>
</head>
<body>
  <article class="brochure">
    <div class="brochure__panel">
      <section class="intro">
        <figure class="photo photo--black-dog"><div class="photo__fill" role="img" aria-label="Photo of a black therapy dog sitting before a brick wall"></div></figure>
        <figure class="photo photo--white-dog"><div class="photo__fill" role="img" aria-label="Photo of a cream therapy dog resting on a blue chair"></div></figure>
        <div class="leaf-mark" role="img" aria-label="Red leaf ornament"></div>
        <h2 class="intro__title">What is Canine Assisted Therapy?</h2>
        <p class="intro__text">Canine Assisted Therapy (CAT) is<br>a unique form of therapy that<br>integrates trained therapy dogs<br>into the healing process.&nbsp; By<br>working alongside licensed<br>therapists, these compassionate<br>and well-trained dogs help<br>support individuals in<br>overcoming emotional, physical,<br>and psychological challenges.<br>This innovative approach<br>promotes healing, reduces<br>stress, and enhances overall<br>well-being.</p>
      </section>

      <section class="benefits">
        <h2 class="section-title">Benefits of Canine Assisted Therapy</h2>
        <ul class="point-list">
          <li><strong>Emotional Support and Comfort.</strong>&nbsp; Therapy dogs provide immediate emotional<br>support, offering comfort and companionship during therapy sessions.<br>Their calming presence helps reduce feelings of anxiety, stress, and depression,<br>and grief, creating a safe and nurturing environment for healing.</li>
          <li><strong>Stress Relief and Relaxation.</strong>&nbsp; Interacting with dogs has been proven to reduce<br>cortisol (stress hormone) levels and increase serotonin and oxytocin, the “feel-good”<br>hormones.&nbsp; This natural relief from stress makes Canine Assisted Therapy<br>an ideal option for individuals dealing with anxiety, trauma, PTSD, and grief.</li>
          <li><strong>Improved Mental Health.</strong>&nbsp; Therapy dogs encourage social interaction,<br>communication, and emotional expression, helping individuals address<br>mental health challenges such as depression, anxiety, PTSD, and grief.<br>The unconditional love and companionship of a dog can foster trust and<br>openness during therapy sessions.</li>
        </ul>
      </section>

      <section class="why">
        <h2 class="section-title">Why Choose Canine Assisted Therapy?</h2>
        <ul class="point-list">
          <li><strong>Proven Effectiveness:</strong> Studies and testimonials highlight the positive effects<br>therapy dogs have on emotional, psychological and physical health.</li>
          <li><strong>Non-Invasive and Gentle:</strong> Therapy dogs provide a natural and non-threatening<br>way to engage with patients, making it accessible for individuals who may feel<br>apprehensive about traditional therapy methods.</li>
          <li><strong>Safe and Trustworthy:</strong> All therapy dogs are carefully trained to work with<br>professionals, ensuring that interactions are safe, beneficial, and appropriate for<br>all individuals.</li>
        </ul>
      </section>
    </div>
  </article>
</body>
</html>
```